Business and Success Coaching Business Card

Need a business card for my coaching business. I coach small businesses, career professionals and, individuals wanting to unlock their human potential and achieve excellence. At the heart of our methodology is the Shaping Purposeful Action Routines Knowingly (SPARK) approach to formulate empowerment, create principles for success and setting achievable outcomes. I would like something that incorporates our new logo, something clean and sharp with a solid darker, but complementary background, color on the card front. The back should be white where there will be room for three questions

Target Market(s)

People looking to advance and improve themselves through a success coach

Industry/Entity Type

Life Coaching

Contact Information for Business Card

Contact information on card.
Business name on front of card
Questions on back

Font styles to use
Other font styles liked:
• Century Gothic or other Serif style fonts that look similar to Century Gothic

Colors

Designer to choose colors to be used in the design.

Requirements
Must have
• Logo on front of card
• Business name - The Steady Forge
• Contact name - Ted Harlow
• Address - Box 4619, Littleton, CO 80127-4619
• Phone number - 303-555-0147
• Email address - harlow.ted@thesteadyforge.example
• Certifications - CSC, CCHt, PTT, PNLP
• Back of card
• Three questions on the back of the card:
• If you were at your best, what would you do right now?
• What is the decision you have been avoiding?
• What's one action you could take in the next 10 minutes?
Nice to have
• I would like to see a solid color on the front of the card that compliments the logo.
• Back should be white, or could be contrasting, but need to have the three questions.

```html
<!DOCTYPE html>
<html lang="en">
<head>
<meta charset="utf-8">
<title>The Steady Forge – Business Card</title>
<link rel="stylesheet" href="https://fonts.googleapis.com/css2?family=Oswald:wght@500;600&family=Didact+Gothic&family=Montserrat:wght@600;700&display=swap">
<style>
  :root {
    --navy: #1f3266;
    --blue: #4a86c8;
    --charcoal: #262626;
    --paper: #f7f7f8;
    --white: #ffffff;
    --stage: #ffffff;
  }
  * { margin: 0; padding: 0; box-sizing: border-box; }
  html, body { width: 1200px; height: 1000px; overflow: hidden; background: var(--stage); }
  .canvas { position: relative; width: 1200px; height: 1000px; }

  .card {
    position: absolute; left: 185px; width: 788px; height: 450px;
    border-top: 6px solid var(--navy); border-bottom: 6px solid var(--navy);
    box-shadow: 0 3px 10px rgba(0,0,0,.35);
    overflow: hidden;
  }
  .card--back { top: 39px; background: var(--paper); }
  .card--front { top: 513px; background: var(--charcoal); }

  .brand-mark {
    position: absolute; border-radius: 50%; background: var(--navy);
  }
  .card--back .brand-mark { left: 325px; top: 70px; width: 130px; height: 130px; }
  .card--front .brand-mark { left: 152px; top: 125px; width: 120px; height: 120px; }

  .brand-name {
    position: absolute; font-family: "Oswald", "Arial Narrow", sans-serif;
    font-weight: 600; text-transform: uppercase; white-space: nowrap;
  }
  .card--back .brand-name {
    left: 0; right: 0; top: 268px; text-align: center;
    font-size: 40px; color: var(--blue); letter-spacing: .5px;
  }
  .card--front .brand-name {
    left: 62px; width: 300px; top: 266px; text-align: center;
    font-size: 28px; color: var(--white);
  }

  .questions {
    position: absolute; left: 0; right: 0; top: 350px; list-style: none;
    text-align: center; font-family: "Didact Gothic", "Century Gothic", sans-serif;
    font-size: 16px; line-height: 25.5px; color: var(--blue); letter-spacing: .6px;
  }

  .divider {
    position: absolute; left: 394px; top: 100px; width: 5px; height: 242px;
    background: var(--blue); border-radius: 3px;
  }

  .person-name {
    position: absolute; left: 452px; top: 90px;
    font-family: "Oswald", "Arial Narrow", sans-serif; font-weight: 500;
    font-size: 31px; letter-spacing: 3px; color: var(--blue); text-transform: uppercase;
  }
  .credentials {
    position: absolute; left: 474px; top: 130px;
    font-family: "Montserrat", "Century Gothic", sans-serif; font-weight: 700;
    font-size: 14px; letter-spacing: 1.5px; color: var(--white);
  }

  .contact-list {
    position: absolute; left: 426px; top: 233px; list-style: none;
    font-family: "Montserrat", "Century Gothic", sans-serif; font-weight: 600;
    font-size: 13px; letter-spacing: 1px; color: var(--white);
  }
  .contact-item { display: flex; align-items: center; height: 25px; }
  .contact-icon { width: 20px; height: 20px; margin-right: 6px; flex: none; }
  .contact-icon path, .contact-icon rect, .contact-icon circle {
    fill: none; stroke: var(--blue); stroke-width: 1.5;
  }
</style>
</head>
<body>
<main class="canvas">

  <section class="card card--back" aria-label="Card back">
    <span class="brand-mark" aria-hidden="true"></span>
    <h2 class="brand-name">The Steady Forge</h2>
    <ul class="questions">
      <li>If You Were At Your Best, What Would You Do Right Now?</li>
      <li>What Is The Decision You Have Been Avoiding?</li>
      <li>What’s One Action You Could Take In The Next 10 Minutes?</li>
    </ul>
  </section>

  <section class="card card--front" aria-label="Card front">
    <span class="brand-mark" aria-hidden="true"></span>
    <h1 class="brand-name">The Steady Forge</h1>
    <span class="divider" aria-hidden="true"></span>

    <p class="person-name">Ted Harlow</p>
    <p class="credentials">CSC, CCHt, PTT, PNLP</p>

    <ul class="contact-list">
      <li class="contact-item">
        <svg class="contact-icon" viewBox="0 0 20 20" aria-hidden="true">
          <rect x="5.5" y="1.5" width="9" height="17" rx="1.5"/>
          <path d="M5.5 15h9M5.5 4h9"/>
        </svg>
        303-555-0147
      </li>
      <li class="contact-item">
        <svg class="contact-icon" viewBox="0 0 20 20" aria-hidden="true">
          <rect x="1.5" y="4.5" width="17" height="11"/>
          <path d="M1.5 4.5l8.5 7 8.5-7"/>
        </svg>
        harlow.ted@thesteadyforge.example
      </li>
      <li class="contact-item">
        <svg class="contact-icon" viewBox="0 0 20 20" aria-hidden="true">
          <path d="M10 17s-5-5.5-5-9a5 5 0 0 1 10 0c0 3.5-5 9-5 9z"/>
          <circle cx="10" cy="8" r="1.8"/>
        </svg>
        Box 4619, Littleton, CO 80127-4619
      </li>
    </ul>
  </section>

</main>
</body>
</html>
```